PITCH PRESENTATION for Feature Film Project

A while ago I had some key art designed for me for a film project called Cinderpeak's Heir (I see it's still in the online portfolio for inkharborstudio, who did the original work). I'm now taking that project to a series of pitch meetings at a film festival here in Canada and am putting together a powerpoint presentation.
I would want you to use the original design/aesthetic framework across the 14 pages of the presentation. I have provided the text and some image ideas (there's also one video to insert) that you may or may not use, etc. Probably for a large chunk of the pages - perhaps 6 of the ten - you could just clean it up and create a common background theme on which to place the companion text. Obviously, while making it pretty is a priority, it's also a priority for it to be legible to the people whom I'm pitching the project when it is projected onto a large screen.
I've uploaded a draft of the powerpoint text - there could be some minor changes between now and next week. I'll be leaving for the festival on December 3 so, obviously need a final version before that date. I've attached a .jpg of the original artwork along with the powerpoint.

Let me know if you need more details.

I wasn't able to upload the .psd file of the original poster artwork with layers & fonts but here is a link to download it from my dropbox: https://www.boxferrycloud.net/s/k3p8q2rz7tw5xym/GH-Cinderpeak%27s%20Heir%20poster.psd?dl=0 best Derek

This is targeted at some Chinese studio executives to whom the project will be pitched. It is for a film that is a martial arts thriller.

Festival

• The main thing is to use the already-existing material (the poster - incl colour scheme and fonts) as the aesthetic foundation for the presentation. We are, in a sense, trying to strengthen the brand identity of the project with the execs.

```html
<!DOCTYPE html>
<html lang="en">
<head>
<meta charset="utf-8">
<title>Cinderpeak's Heir – Pitch Slides</title>
<link rel="stylesheet" href="https://fonts.googleapis.com/css2?family=Tinos&family=Carlito:wght@400;700&display=swap">
<style>
  :root {
    --stage: #8a6440;
    --parchment: #e4c583;
    --parchment-edge: #d6b06a;
    --rust: #c4563a;
    --crimson: #c0323f;
    --paper-white: #fbf6ee;
    --ink: #1f1a14;
    --cream-text: #fbf1e4;
    --frame: #ffffff;
  }
  * { box-sizing: border-box; margin: 0; padding: 0; }
  html, body { width: 1200px; height: 1000px; overflow: hidden; }
  body { background: var(--stage); position: relative; font-family: "Carlito", "Calibri", sans-serif; }

  .slide {
    position: absolute;
    background: radial-gradient(circle at 40% 40%, var(--parchment), var(--parchment-edge));
    box-shadow: 0 6px 18px rgba(0,0,0,.45);
    overflow: hidden;
  }
  .slide--characters { left: 10px; top: 0; width: 723px; height: 540px; }
  .slide--business { left: 467px; top: 450px; width: 733px; height: 550px; }

  /* torn paper banners: white underlayer + coloured fill */
  .torn {
    position: absolute;
    background: var(--paper-white);
    padding-bottom: 5px;
    clip-path: polygon(0 4%, 10% 0, 24% 3%, 38% 0, 52% 4%, 66% 1%, 80% 4%, 92% 0, 100% 3%, 100% 94%, 94% 99%, 86% 95%, 77% 100%, 68% 95%, 59% 99%, 50% 94%, 41% 100%, 32% 95%, 23% 99%, 14% 94%, 6% 99%, 0 95%);
  }
  .torn__fill {
    height: 100%;
    display: flex; align-items: center; justify-content: center;
    clip-path: polygon(0 0, 100% 0, 100% 92%, 93% 97%, 85% 93%, 76% 98%, 67% 93%, 58% 97%, 49% 92%, 40% 98%, 31% 93%, 22% 97%, 13% 92%, 5% 97%, 0 93%);
  }
  .title-banner .torn__fill { background: var(--rust); }
  .title-banner h1 {
    font-family: "Tinos", "Times New Roman", serif;
    font-weight: 400; font-size: 45px; letter-spacing: 1px;
    color: var(--cream-text);
  }
  .slide--characters .title-banner { left: 0; top: 28px; width: 723px; height: 82px; }
  .slide--business .title-banner { left: 0; top: 18px; width: 733px; height: 94px; }

  .name-banner .torn__fill { background: var(--crimson); }
  .name-banner h2 {
    font-weight: 400; font-size: 28px; color: var(--cream-text);
  }
  .name-banner--left { left: 2px; top: 148px; width: 265px; height: 66px; }
  .name-banner--left .torn__fill { justify-content: flex-start; padding-left: 30px; }
  .name-banner--right { left: 433px; top: 148px; width: 290px; height: 60px; }

  .photo-frame {
    position: absolute;
    background: var(--frame);
    padding: 6px;
    box-shadow: 0 2px 6px rgba(0,0,0,.3);
  }
  .photo-frame .fill { width: 100%; height: 100%; }
  .portrait--left { left: 32px; top: 233px; width: 291px; height: 228px; }
  .portrait--left .fill { background: linear-gradient(135deg, #2b2a3a, #0c0c12 70%); }
  .portrait--right { left: 437px; top: 220px; width: 270px; height: 240px; }
  .portrait--right .fill { background: radial-gradient(circle at 55% 45%, #8a8f9c, #3c414e 75%); }

  .intro {
    position: absolute; left: 40px; top: 128px; width: 653px;
    text-align: center; font-size: 15px; line-height: 20px; color: var(--ink);
  }

  .poster--fists { left: 13px; top: 173px; width: 111px; height: 170px; }
  .poster--fists .fill { background: linear-gradient(180deg, #4a4a4e, #d8d8d8 55%, #2a2a2c); }
  .poster--crossline { left: 513px; top: 167px; width: 119px; height: 183px; }
  .poster--crossline .fill { background: linear-gradient(160deg, #6b6b6b, #c96a3c 45%, #dcdcdc 70%, #9a9a9a); }
  .poster--jade { left: 13px; top: 368px; width: 114px; height: 154px; }
  .poster--jade .fill { background: linear-gradient(180deg, #4b3a2a, #8c5a34 50%, #c08a3a); }

  .film-card {
    position: absolute;
    background: var(--paper-white);
    padding-bottom: 5px;
    clip-path: polygon(0 2%, 12% 0, 30% 3%, 48% 0, 66% 2%, 84% 0, 100% 3%, 100% 96%, 92% 100%, 82% 97%, 70% 100%, 58% 96%, 46% 100%, 34% 97%, 22% 100%, 10% 96%, 0 99%);
  }
  .film-card__body {
    height: 100%; background: var(--crimson);
    color: var(--cream-text);
    font-size: 15px; line-height: 20px;
    padding: 16px 14px 0;
  }
  .film-card__title { font-weight: 700; }
  .film-card .gap { height: 20px; }
  .card--fists { left: 140px; top: 182px; width: 296px; height: 145px; }
  .card--jade { left: 140px; top: 382px; width: 268px; height: 140px; }
  .card--jade .film-card__body { padding-top: 28px; }
  .card--crossline { left: 450px; top: 376px; width: 266px; height: 144px; }
</style>
</head>
<body>

  <section class="slide slide--characters">
    <div class="torn title-banner"><div class="torn__fill"><h1>KEY CHARACTERS</h1></div></div>

    <div class="torn name-banner name-banner--left"><div class="torn__fill"><h2>Kai-Ming Loh</h2></div></div>
    <div class="torn name-banner name-banner--right"><div class="torn__fill"><h2>Tobin Wren</h2></div></div>

    <div class="photo-frame portrait--left">
      <div class="fill" role="img" aria-label="Portrait of actor Kai-Ming Loh in a striped suit, dark moody lighting"></div>
    </div>
    <div class="photo-frame portrait--right">
      <div class="fill" role="img" aria-label="Portrait of actor Tobin Wren in a grey three-piece suit against a grey backdrop"></div>
    </div>
  </section>

  <section class="slide slide--business">
    <div class="torn title-banner"><div class="torn__fill"><h1>THE BUSINESS SIDE</h1></div></div>

    <p class="intro">Martial arts films have a solid fan base internationally. And female-led thrillers have a proven track record.</p>

    <div class="photo-frame poster--fists">
      <div class="fill" role="img" aria-label="Poster for The Lord With The Copper Palms"></div>
    </div>
    <div class="film-card card--fists">
      <div class="film-card__body">
        <p class="film-card__title">The Lord With The Copper Palms (2012)</p>
        <p>Estimated budget (incl P&amp;A): $15M</p>
        <div class="gap"></div>
        <p>International box office: $22M</p>
        <p>Domestic DVD/Blu-ray: $11.5M</p>
      </div>
    </div>

    <div class="photo-frame poster--crossline">
      <div class="fill" role="img" aria-label="Poster for Crossline"></div>
    </div>

    <div class="photo-frame poster--jade">
      <div class="fill" role="img" aria-label="Poster for Jade Step One"></div>
    </div>
    <div class="film-card card--jade">
      <div class="film-card__body">
        <p class="film-card__title">Jade Step One (2012)</p>
        <p>Estimated budget: $12M</p>
        <div class="gap"></div>
        <p>International box office: $25M</p>
      </div>
    </div>

    <div class="film-card card--crossline">
      <div class="film-card__body">
        <p class="film-card__title">Crossline (2012)</p>
        <p>Estimated budget: $23M</p>
        <div class="gap"></div>
        <p>International box office: $34.5M</p>
        <p>Domestic DVD/Blu-ray: $9.5M</p>
      </div>
    </div>
  </section>

</body>
</html>
```